Lumora! Consulting

We need a web design for a new supply chain consulting business. we will work with major brands in the electronics, apparel, toy and jewelry industries to create a sustainability program for our customers and implement in their supply chain. We want our customers to have confidence in their supply chain responsibility program. We also manage stakeholder engagements, NGO relationships, and external communications.

I would like to colors to be green, orange and/or black to match the logo (attached). The final design should communicate positive and optimistic leadership - for a professional, sustainable, business.

Industry/Entity Type

Business

```html
<!DOCTYPE html>
<html lang="en">
<head>
<meta charset="utf-8">
<title>Lumora! Consulting</title>
<link href="https://fonts.googleapis.com/css2?family=Abel&family=Open+Sans:wght@400;600;700&display=swap" rel="stylesheet">
<style>
:root{
  --orange:#f0931b;
  --orange-deep:#ee8a0e;
  --green:#8cc63f;
  --green-line:#7db53a;
  --text-grey:#9a9a9a;
  --light-band:#ededed;
  --card-border:#e3e3e3;
  --footer:#434343;
  --footer-bar:#353535;
  --footer-text:#a9a9a9;
  --white:#ffffff;
}
*{box-sizing:border-box;margin:0;padding:0}
html,body{width:760px;height:1200px;overflow:hidden;background:var(--white)}
body{position:relative;font-family:"Open Sans",Arial,sans-serif;color:var(--text-grey)}
.abs{position:absolute}

.top-rule{left:0;top:0;width:760px;height:3px;background:var(--green-line)}
.site-header{left:0;top:3px;width:760px;height:93px;background:var(--white)}
.brand{left:62px;top:18px;display:flex;align-items:center;gap:8px}
.brand-dot{width:22px;height:22px;border-radius:50%;background:var(--green)}
.brand-name{font-size:28px;font-weight:400;color:var(--orange)}
.main-nav{left:458px;top:35px;display:flex;align-items:center;font-family:"Abel",Arial,sans-serif;font-size:12px}
.main-nav a{color:var(--orange);text-decoration:none;padding:5px 8px;line-height:14px;margin-right:4px}
.main-nav a.current{background:var(--orange);color:var(--white);border-radius:3px;padding:5px 10px}

.hero{left:0;top:96px;width:760px;height:282px;background:linear-gradient(90deg,#4b5a6b 0%,#c9d6e2 35%,#e7eef4 60%,#b7c2cc 85%,#5b4a44 100%)}

.about-title{left:0;top:396px;width:760px;text-align:center;font-size:19px;color:var(--orange);letter-spacing:.5px}
.about-text{left:68px;top:422px;width:624px;text-align:center;font-size:8.5px;line-height:12px;color:var(--text-grey)}
.btn{background:var(--orange-deep);color:var(--white);font-weight:600;text-align:center;font-size:9.5px;display:flex;align-items:center;justify-content:center}
.about-btn{left:344px;top:473px;width:72px;height:29px}

.services{left:0;top:522px;width:760px;height:158px;background:var(--green)}
.service{top:14px;width:220px;text-align:center;color:var(--white)}
.service svg{display:block;margin:0 auto}
.service h3{font-weight:400;font-size:18px;margin-top:11px;letter-spacing:.3px}
.service p{font-size:8.3px;font-weight:600;line-height:11.5px;margin-top:6px}

.posts-title{left:57px;top:698px;font-size:18px;color:var(--orange);font-weight:400}
.post-card{top:725px;height:140px;border:1px solid var(--card-border);border-radius:3px;background:var(--white)}
.post-card h4{position:absolute;left:8px;top:9px;font-size:17.5px;font-weight:400;color:var(--orange)}
.post-thumb{left:9px;top:37px;width:137px;height:85px;background:linear-gradient(135deg,#e6ecf2,#9fb0c2 55%,#3a4654)}
.post-card p{position:absolute;font-size:8.3px;line-height:11.3px;color:var(--text-grey)}

.blog-band{left:0;top:888px;width:760px;height:70px;background:var(--light-band)}
.blog-btn{left:296px;top:907px;width:168px;height:30px}

.edit-link{left:57px;top:977px;font-size:8.5px;color:var(--orange)}

.site-footer{left:0;top:1005px;width:760px;height:173px;background:var(--footer)}
.foot-col{top:24px;width:158px}
.foot-col h5{font-weight:400;font-size:14px;color:var(--footer-text);border-bottom:1px solid var(--footer-text);padding-bottom:1px}
.sitemap li{list-style:none;font-size:7.5px;font-weight:600;color:var(--footer-text);margin:12px 0 0 3px}
.foot-news h6{font-weight:400;font-size:10.5px;color:var(--footer-text);margin-top:4px}
.foot-news p,.foot-contact p{font-size:8px;line-height:11px;color:#8d8d8d}
.foot-brand{left:572px;top:35px;display:flex;align-items:center;gap:7px}
.foot-brand .brand-dot{width:16px;height:16px;background:var(--white)}
.foot-brand span{font-size:25px;color:var(--white)}
.social-dot{left:578px;top:117px;width:10px;height:10px;border-radius:50%;background:#8d8d8d}
.footer-bar{left:0;top:1178px;width:760px;height:22px;background:var(--footer-bar);text-align:center;font-size:8px;line-height:22px;color:var(--footer-text)}
</style>
</head>
<body>
<div class="abs top-rule"></div>
<header class="abs site-header">
  <div class="abs brand"><span class="brand-dot"></span><span class="brand-name">Lumora!</span></div>
  <nav class="abs main-nav">
    <a class="current" href="#">Home</a><a href="#">Services</a><a href="#">Contact</a><a href="#">About</a><a href="#">News</a>
  </nav>
</header>

<div class="abs hero" role="img" aria-label="Photo of a business team meeting in front of a screen showing a bar chart"></div>

<h2 class="abs about-title">ABOUT</h2>
<p class="abs about-text">Lorem ipsum dolor sit amet, consectetur adipiscing elit, sed do eiusmod tempor incididunt ut labore et dolore magna aliqua. Ut enim ad minim veniam, quis nostrud exercitation ullamco laboris nisi ut aliquip ex ea commodo consequat.</p>
<div class="abs btn about-btn">More Info</div>

<section class="abs services">
  <div class="abs service" style="left:48px">
    <svg width="46" height="46" viewBox="0 0 46 46" fill="none" stroke="#fff" stroke-width="1.6"><circle cx="23" cy="23" r="21.5"/><circle cx="23" cy="23" r="10" fill="#fff"/><path d="M17 19c3 0 4 2 6 1s2 3 0 5-1 4-3 4M26 15c1 2 3 2 4 4" stroke="#8cc63f" stroke-width="1.8"/></svg>
    <h3>SERVICE 1</h3>
    <p>I am text block. Click edit button to change this text. Lorem ipsum dolor sit amet, consectetur adipiscing elit. Ut elit tellus, luctus nec ullamcorper mattis, pulvinar dapibus leo.</p>
  </div>
  <div class="abs service" style="left:270px">
    <svg width="46" height="46" viewBox="0 0 46 46" fill="none" stroke="#fff" stroke-width="1.6"><circle cx="23" cy="23" r="21.5"/><path d="M16 30l2-6 10-10 4 4-10 10z M26 16l4 4" fill="#fff" stroke-linejoin="round"/><path d="M26 16l4 4" stroke="#8cc63f"/></svg>
    <h3>SERVICE 2</h3>
    <p>I am text block. Click edit button to change this text. Lorem ipsum dolor sit amet, consectetur adipiscing elit. Ut elit tellus, luctus nec ullamcorper mattis, pulvinar dapibus leo.</p>
  </div>
  <div class="abs service" style="left:492px">
    <svg width="46" height="46" viewBox="0 0 46 46" fill="none" stroke="#fff" stroke-width="1.6"><circle cx="23" cy="23" r="21.5"/><g fill="#fff" stroke="none"><rect x="14" y="27" width="3" height="5"/><rect x="19" y="24" width="3" height="8"/><rect x="24" y="21" width="3" height="11"/><rect x="29" y="18" width="3" height="14"/></g><path d="M14 23l6-5 4 2 8-7M28 13h4v4"/></svg>
    <h3>SERVICE 3</h3>
    <p>I am text block. Click edit button to change this text. Lorem ipsum dolor sit amet, consectetur adipiscing elit. Ut elit tellus, luctus nec ullamcorper mattis, pulvinar dapibus leo.</p>
  </div>
</section>

<h2 class="abs posts-title">Latest Posts</h2>
<article class="abs post-card" style="left:57px;width:316px">
  <h4>Testing Text</h4>
  <div class="abs post-thumb" role="img" aria-label="Photo of colleagues in a business meeting"></div>
  <p style="left:153px;top:33px;width:156px">Lorem ipsum dolor sit amet, consectetur adipiscing elit, sed do eiusmod tempor incididunt ut labore et dolore magna aliqua. Ut enim ad minim veniam, quis nostrud exercitation ullamco laboris nisi ut aliquip ex ea commodo consequat. Duis aute irure dolor in reprehenderit in voluptate</p>
</article>
<article class="abs post-card" style="left:381px;width:316px">
  <h4>Welcome to Lumora</h4>
  <p style="left:8px;top:33px;width:300px">Sed ut perspiciatis unde omnis iste natus error sit voluptatem accusantium doloremque laudantium, totam rem aperiam, eaque ipsa quae ab illo inventore veritatis et quasi architecto beatae vitae dicta sunt explicabo. Nemo enim ipsam voluptatem quia voluptas sit aspernatur aut odit aut fugit, sed quia consequuntur magni dolores eos qui ratione voluptatem sequi nesciunt.</p>
</article>

<div class="abs blog-band"></div>
<div class="abs btn blog-btn">Read More From Blog! Click Here!</div>

<a class="abs edit-link">(Edit) Edit with Layout Studio</a>

<footer class="abs site-footer">
  <div class="abs foot-col sitemap" style="left:48px">
    <h5>Sitemap</h5>
    <ul><li>Home</li><li>Services</li><li>Contact</li><li>About</li><li>News</li></ul>
  </div>
  <div class="abs foot-col foot-news" style="left:217px">
    <h5>News</h5>
    <h6>Testing Text</h6>
    <p>Lorem ipsum dolor sit amet,<br>consectetur...</p>
    <h6 style="margin-top:8px">Welcome to Lumora</h6>
    <p>Sed ut perspiciatis unde omnis iste<br>natu...</p>
  </div>
  <div class="abs foot-col foot-contact" style="left:386px">
    <h5>Contact</h5>
    <p style="margin-top:6px">Address: Complete Adrees Here<br>Phone: 123.456.7890<br>Email: contact@lumora.com</p>
  </div>
  <div class="abs foot-brand"><span class="brand-dot"></span><span>Lumora!</span></div>
  <div class="abs social-dot"></div>
</footer>
<div class="abs footer-bar">© 2014 Lumora!. All Rights Reserved.</div>
</body>
</html>
```